An anniversary gift for my girlfriend

My girlfriend and I have been dating for almost 2 years. We met online and this has afforded us the really unique opportunity to have the first words we said to each other (the whole conversation, in fact) preserved. We're moving in together in a few months and she doesn't know that I saved the conversation. I've been waiting for this to turn it into something we can hang in our new place.

The only phrase I want to use is:
"Well if you dislike people's knees then I think we'll get along famously"

It's an Nobody Leaves Before Midnight in Portland reference for the curious.

I want the poster to use the words themselves as the art; I'm thinking typography. I'd like it to match her aesthetic, she likes to wear Nora Vell and T. Brisk. Colors shouldn't be anything too "girly". Somewhere I'd like to include the date June 1, 2015. It shouldn't be a major piece of the poster though, just a way to denote the date.

It should fit (and be fully visible in) a 16x20 (inches) frame

Thanks in advance for the work!

Requirements
Must have
• Must use only the words: "Well if you dislike people's knees then I think we'll get along famously"
• I want this to be typography, so making the phrase the center of the poster and the art itself.

```html
<!DOCTYPE html>
<html lang="en">
<head>
<meta charset="utf-8">
<title>Well If You Dislike People's Knees — Anniversary Poster</title>
<link rel="stylesheet" href="https://fonts.googleapis.com/css2?family=Roboto+Slab:wght@300;700&display=swap">
<style>
  :root {
    --backdrop: #ececec;
    --paper: #ffffff;
    --wash-peach: #fbe7dc;
    --wash-lilac: #f1edf8;
    --wash-blue: #d6e3f5;
    --wash-cream: #f8eedd;
    --band-cyan: #5ad8e4;
    --band-purple: #8a4fa6;
    --band-teal: #2aa8c0;
    --band-red: #e8353a;
    --band-magenta: #c51f6b;
    --ink-red: #e0312a;
    --ink-yellow: #f2b51c;
    --ink-grey: #9a9a9a;
    --ink-purple: #8e1a7d;
    --ink-brown: #4a2120;
    --ink-magenta: #e0177a;
    --ink-lime: #93c130;
    --ink-teal: #2fb0c6;
    --ink-orange: #f0602a;
    --ink-pink: #d06aa3;
    --ink-date: #1a1a1a;
  }
  * { margin: 0; padding: 0; box-sizing: border-box; }
  html, body {
    width: 1200px;
    height: 1148px;
    overflow: hidden;
    background: var(--backdrop);
  }
  .poster {
    position: absolute;
    left: 160px;
    top: 24px;
    width: 880px;
    height: 1100px;
    background: var(--paper);
    overflow: hidden;
  }
  .poster-wash {
    position: absolute;
    left: 0;
    top: 0;
    width: 880px;
    height: 980px;
    background:
      linear-gradient(180deg, rgba(255,255,255,0) 65%, var(--wash-cream) 100%),
      linear-gradient(90deg, var(--wash-peach) 0%, var(--wash-lilac) 45%, var(--paper) 60%, var(--wash-blue) 100%);
  }
  .poster-bands {
    position: absolute;
    left: 0;
    top: 980px;
    width: 880px;
    height: 120px;
    background: linear-gradient(90deg, var(--band-purple) 0%, var(--band-teal) 35%, var(--band-red) 60%, var(--band-magenta) 100%);
  }
  .phrase {
    position: absolute;
    left: 0;
    top: 104px;
    width: 880px;
    display: flex;
    flex-direction: column;
    align-items: center;
    font-family: "Roboto Slab", serif;
    font-weight: 300;
    line-height: 0.8;
    letter-spacing: -0.02em;
    text-transform: uppercase;
  }
  .phrase-line {
    display: block;
    transform: scaleX(0.82);
    white-space: nowrap;
  }
  .line-well      { color: var(--ink-red);     font-size: 110px; }
  .line-if-you    { color: var(--ink-yellow);  font-size: 96px; }
  .line-dislike   { color: var(--ink-grey);    font-size: 99px; }
  .line-peoples   { color: var(--ink-purple);  font-size: 90px; }
  .line-knees     { color: var(--ink-brown);   font-size: 110px; }
  .line-then      { color: var(--ink-magenta); font-size: 115px; }
  .line-i-think   { color: var(--ink-lime);    font-size: 104px; }
  .line-well-2    { color: var(--ink-teal);    font-size: 104px; }
  .line-get-along { color: var(--ink-orange);  font-size: 76px; }
  .line-famously  { color: var(--ink-pink);    font-size: 72px; }
  .date {
    margin-top: 26px;
    font-family: "Roboto Slab", serif;
    font-weight: 700;
    font-size: 20px;
    letter-spacing: 0.02em;
    color: var(--ink-date);
  }
</style>
</head>
<body>
  <main class="poster">
    <div class="poster-wash" role="img" aria-label="Soft pastel light beams in peach, lilac and pale blue"></div>
    <div class="poster-bands" role="img" aria-label="Colourful angular bands in cyan, purple, teal, red and magenta"></div>

    <h1 class="phrase">
      <span class="phrase-line line-well">Well</span>
      <span class="phrase-line line-if-you">If You</span>
      <span class="phrase-line line-dislike">Dislike</span>
      <span class="phrase-line line-peoples">People's</span>
      <span class="phrase-line line-knees">Knees</span>
      <span class="phrase-line line-then">Then</span>
      <span class="phrase-line line-i-think">I Think</span>
      <span class="phrase-line line-well-2">We'll</span>
      <span class="phrase-line line-get-along">Get Along</span>
      <span class="phrase-line line-famously">Famously</span>
      <time class="date" datetime="2015-06-01">JUNE 1, 2015</time>
    </h1>
  </main>
</body>
</html>
```